Modern Small Law Firm Website To Look Cutting Edge

I need a website design for a new, single-attorney law firm. The firm will be called "The Ashcombe Law Group." Our goal is to handle car accident and general personal injury lawsuits for individuals.

Our selling points are: (1) We charge less so you keep more; (2) We have experience and success trying and settling multi-million dollar cases; (3) We use modern technology to make the whole process simple, easy and hassle-free for clients.

Also because we are a one-man law firm, the clients will personally know the lawyer and have access to them. For that reason, I thought a good big tagline for the website would be "KNOW YOUR LAWYER"

I like the idea of splitting the website vertically down the middle, with the left side having a blue background, a picture of me, and big white lettering for the tagline, and the right side having a white background with blue lettering and headlines. I don't want navy blue or royal blue, but a more bright and eye-catching blue color. We can experiment with different shades.

I would be curious about how it could look with some minor orange accent coloring somewhere.

I need to feature prominently, probably in the top left corner, this phone number: 504-271-9038.

This will be used as much by mobile users as it would be by desktop/computer users.

The final design should communicate trust, convenience and cutting edge technology that leads to success.

Finally, I would be curious how we can have a sleek looking info submission box somewhere on the right side nearer the bottom that features different combinations of presenting these phrases: "QUICK QUESTION? QUICK ANSWER" The info submission button could say "Ask"

I am uploading two different pictures of me that can be used. The gray backgrounds are not necessary or good, if there is a way to cut them out that would be great. I can try and get that if needed.

Target Market(s)

Individuals who have been hurt by others, mostly in car accidents. They will be frustrated, inconvenienced and need to be soothed.

Industry/Entity Type

Legal

Number of Pages Required

1 page

Font styles to use
Sans Serif

Colors
0692cd
33a6d7
85cae6
faa54b
f78f20
3276b5

Requirements
Must have
• If you have started designing already, please note that the project description information is more important than the image that I uploaded originally. It has since been deleted.
• Also please now use the color photo that has been uploaded.
Nice to have
• I really want a clean and simple website design with not a lot of clutter. I'd like to avoid the typical law firm websites that you see that have tool bars across the top and basic borders/columns everywhere. It needs to grab your attention and look a little more cutting edge and different.
• Let's experiment with different eye-catching ways to present the three value propositions I noted.
• Also if the screen is split vertically with the left and right side being blue and white, maybe we can experiment with different ways that the two colors could fade into each other as opposed to just a line where one color starts and the other ends.
• And maybe the blue/white backgrounds could be textured somehow so that they don't appear flat. Perhaps we could try using differing shades of blue to give the appearance of pattern or 3D texture.
Should not have
• The basic picture/design I uploaded is just a suggestion, but there isn't really anything there.

```html
<!DOCTYPE html>
<html lang="en">
<head>
<meta charset="utf-8">
<title>The Ashcombe Law Group — Quick Question</title>
<link href="https://fonts.googleapis.com/css2?family=Raleway:wght@400;500;700;800&display=swap" rel="stylesheet">
<style>
  :root {
    --blue-left: #04a3e6;
    --blue-right: #22b0ea;
    --blue-deep: #0a92d2;
    --blue-text: #0d8fcd;
    --blue-body: #1784bd;
    --blue-panel: #2db2ec;
    --blue-button: #0aa0e4;
    --blue-photo-top: #0b8ccb;
    --blue-photo-bottom: #067fbd;
    --white: #ffffff;
    --field-fill: rgba(255, 255, 255, 0.14);
    --footer: #232323;
    --footer-link: #1aa3e6;
  }
  * { box-sizing: border-box; margin: 0; padding: 0; }
  html, body { width: 1200px; height: 740px; overflow: hidden; }
  body { font-family: "Raleway", Arial, sans-serif; position: relative; background: var(--blue-left); }

  .half-left { position: absolute; left: 0; top: 0; width: 600px; height: 677px; background: var(--blue-left); }
  .half-right {
    position: absolute; left: 600px; top: 0; width: 600px; height: 677px;
    background: linear-gradient(160deg, #27b3ec 0%, #20aee8 55%, #29b4ec 100%);
  }

  .brand {
    position: absolute; left: 0; width: 1200px; top: 28px; text-align: center;
    font-weight: 700; font-size: 40px; color: var(--blue-deep); letter-spacing: -0.5px;
  }

  .phone { position: absolute; left: 924px; top: 25px; display: flex; align-items: center; }
  .phone-icon { width: 48px; height: 48px; border-radius: 50%; background: var(--blue-deep); display: flex; align-items: center; justify-content: center; }
  .phone-number { margin-left: 14px; font-size: 20px; color: var(--blue-text); letter-spacing: 0.3px; }

  .attorney-photo {
    position: absolute; left: 120px; top: 94px; width: 370px; height: 583px;
    background: linear-gradient(180deg, var(--blue-photo-top) 0%, var(--blue-photo-bottom) 100%);
    border-radius: 160px 160px 0 0;
  }

  .tagline-panel {
    position: absolute; left: 81px; top: 380px; width: 438px; height: 209px;
    background: var(--blue-panel); display: flex; align-items: center; justify-content: center;
  }
  .tagline { font-weight: 800; font-size: 50px; line-height: 1.15; text-align: center; color: var(--blue-button); }

  .value { position: absolute; left: 640px; width: 380px; }
  .value-number { position: absolute; left: 18px; top: -8px; font-size: 46px; color: var(--blue-body); }
  .value-slash { position: absolute; left: 0; top: -2px; }
  .value-title { margin-left: 72px; font-size: 22px; color: var(--blue-text); }
  .value-body { margin-left: 72px; margin-top: 8px; font-family: Arial, sans-serif; font-size: 15px; line-height: 24px; color: var(--blue-body); }

  .cta { position: absolute; top: 562px; width: 208px; height: 53px; display: flex; align-items: center; justify-content: center; font-weight: 700; font-size: 16px; }
  .cta-question { left: 641px; border: 1px solid var(--blue-button); color: var(--blue-button); }
  .cta-answer { left: 870px; background: var(--blue-button); color: #5cc6f1; }

  .footer { position: absolute; left: 0; top: 677px; width: 1200px; height: 63px; background: var(--footer); color: var(--white); font-size: 15px; display: flex; align-items: center; justify-content: center; }
  .footer a { color: var(--footer-link); text-decoration: none; }

  .ask-title { position: absolute; left: 0; width: 1200px; top: 106px; text-align: center; color: var(--white); font-size: 41px; font-weight: 400; letter-spacing: 0.5px; }
  .ask-form { position: absolute; left: 392px; top: 196px; width: 416px; }
  .ask-field { width: 416px; height: 52px; border: 1.5px solid rgba(255,255,255,0.85); background: var(--field-fill); color: var(--white); font-family: Arial, sans-serif; font-size: 16px; padding: 0 24px; display: flex; align-items: center; margin-bottom: 10px; }
  .ask-field.message { height: 105px; align-items: flex-start; padding-top: 16px; }
  .ask-button { width: 416px; height: 52px; margin-top: 10px; background: var(--white); color: var(--blue-button); font-weight: 700; font-size: 24px; display: flex; align-items: center; justify-content: center; }
</style>
</head>
<body>
  <div class="half-left"></div>
  <div class="half-right"></div>

  <div class="brand">The Ashcombe Law Group</div>

  <div class="phone">
    <div class="phone-icon">
      <svg width="20" height="20" viewBox="0 0 24 24"><path fill="#4fc2f0" d="M6.6 10.8a15.1 15.1 0 0 0 6.6 6.6l2.2-2.2c.3-.3.7-.4 1-.2 1.1.4 2.3.6 3.6.6.6 0 1 .4 1 1V20c0 .6-.4 1-1 1A17 17 0 0 1 3 4c0-.6.4-1 1-1h3.5c.6 0 1 .4 1 1 0 1.3.2 2.5.6 3.6.1.3 0 .7-.2 1z"/></svg>
    </div>
    <span class="phone-number">504-271-9038</span>
  </div>

  <div class="attorney-photo" role="img" aria-label="Portrait photo of the attorney in suit and tie"></div>

  <div class="tagline-panel"><div class="tagline">"KNOW YOUR<br>LAWYER"</div></div>

  <div class="value" style="top:168px">
    <svg class="value-slash" width="60" height="60"><line x1="0" y1="8" x2="56" y2="58" stroke="#1784bd" stroke-width="1"/></svg>
    <span class="value-number">1</span>
    <div class="value-title">NEVER MORE THAN 24%</div>
    <div class="value-body">Our lawyer will never overcharge you<br>like others will.</div>
  </div>
  <div class="value" style="top:303px">
    <svg class="value-slash" width="60" height="60"><line x1="0" y1="8" x2="56" y2="58" stroke="#1784bd" stroke-width="1"/></svg>
    <span class="value-number">2</span>
    <div class="value-title">WE MAKE IT EASY</div>
    <div class="value-body">These new brake pads are really cool,<br>you won't believe it.</div>
  </div>
  <div class="value" style="top:438px">
    <svg class="value-slash" width="60" height="60"><line x1="0" y1="8" x2="56" y2="58" stroke="#1784bd" stroke-width="1"/></svg>
    <span class="value-number">3</span>
    <div class="value-title">BIG FIRM LAWYERING</div>
    <div class="value-body">With experience in multi-million dollar<br>litigation, we're the best.</div>
  </div>

  <div class="cta cta-question">QUICK QUESTION?</div>
  <div class="cta cta-answer">QUICK ANSWER!</div>

  <footer class="footer">©&nbsp;<a href="#">The Ashcombe Law Group</a>&nbsp;- 2016 All rights reserved</footer>

  <h1 class="ask-title">QUICK QUESTION?</h1>
  <div class="ask-form">
    <div class="ask-field">Enter Your Name</div>
    <div class="ask-field">Enter Your Phone</div>
    <div class="ask-field">Enter Your E-mail</div>
    <div class="ask-field message">Enter Your Message</div>
    <div class="ask-button">ASK</div>
  </div>
</body>
</html>
```